Property Consultancy require stationary

Property Consultancy K7 Group Ltd, slogan is Bright Harbour Allies. Require letterhead, business card and Outlook email signature utilising existing logo design.

Property

```html
<!DOCTYPE html>
<html lang="en">
<head>
<meta charset="utf-8">
<title>K7 Group Ltd — Business Card</title>
<link href="https://fonts.googleapis.com/css2?family=Roboto:wght@300;400;700&display=swap" rel="stylesheet">
<style>
  :root {
    --page-bg: #d9d6d1;
    --card-dark: #262626;
    --card-light: #e9e9e9;
    --brand-red: #c3222a;
    --brand-charcoal: #3a3a3a;
    --text-grey: #5a5a5a;
    --text-soft: #9a9a9a;
    --text-on-dark: #d4d4d4;
  }
  * { box-sizing: border-box; margin: 0; padding: 0; }
  html, body {
    width: 1200px; height: 900px; overflow: hidden;
    background: var(--page-bg);
    font-family: "Roboto", Arial, sans-serif;
  }
  .stationery {
    width: 1200px; height: 900px;
    display: flex; flex-direction: column; align-items: center; justify-content: center;
    gap: 44px;
  }
  .card {
    width: 600px; height: 333px; position: relative; overflow: hidden;
    box-shadow: 0 6px 18px rgba(0,0,0,0.18);
  }
  .card--back { background: var(--card-dark); }
  .card--front { background: var(--card-light); }

  .brand { display: flex; flex-direction: column; align-items: flex-start; }
  .brand__name {
    display: flex; align-items: center; gap: 12px;
    font-weight: 300; font-size: 46px; letter-spacing: 3px; line-height: 1;
  }
  .brand__mark { width: 22px; height: 22px; background: var(--brand-red); }
  .brand__tagline {
    margin-top: 8px; font-weight: 300; font-size: 11px;
    letter-spacing: 2.4px; text-transform: uppercase; color: var(--text-soft);
  }

  .card--back .brand {
    position: absolute; left: 50%; top: 108px; transform: translateX(-50%);
  }
  .card--back .brand__name { color: var(--text-on-dark); }
  .card--back .web {
    position: absolute; left: 0; right: 0; top: 236px; text-align: center;
    font-size: 13px; color: var(--text-on-dark); letter-spacing: 0.5px;
  }

  .card--front .brand { position: absolute; left: 40px; top: 160px; }
  .card--front .brand__name { color: var(--text-grey); }

  .contact {
    position: absolute; left: 372px; top: 40px; color: var(--text-grey);
    font-size: 12px; font-weight: 300; line-height: 1.35;
  }
  .contact__name { font-size: 15px; font-weight: 400; }
  .contact__lines { margin-top: 14px; list-style: none; }
  .contact__lines li { display: flex; gap: 8px; }
  .contact__key { color: var(--brand-red); width: 10px; }

  .web { font-weight: 300; }
  .web strong { font-weight: 700; }
  .card--front .web {
    position: absolute; right: 36px; top: 210px; font-size: 12px; color: var(--text-grey);
  }

  .accent-band {
    position: absolute; left: 0; right: 0; bottom: 0; height: 16px; display: flex;
  }
  .accent-band__dark { flex: 0 0 48%; background: var(--brand-charcoal); }
  .accent-band__red { flex: 1; background: var(--brand-red); }
</style>
</head>
<body>
  <main class="stationery">
    <section class="card card--back" aria-label="Business card back">
      <div class="brand">
        <div class="brand__name"><span class="brand__mark"></span>K7 GROUP</div>
        <div class="brand__tagline">Bright Harbour Allies</div>
      </div>
      <p class="web">www.<strong>k7group</strong>.co.nz</p>
    </section>

    <section class="card card--front" aria-label="Business card front">
      <div class="brand">
        <div class="brand__name"><span class="brand__mark"></span>K7 GROUP</div>
        <div class="brand__tagline">Bright Harbour Allies</div>
      </div>

      <div class="contact">
        <p class="contact__name">Martin Hale-Rossiter</p>
        <p>BCom (Prop) MRIA</p>
        <p>Director</p>
        <ul class="contact__lines">
          <li><span class="contact__key">T</span>+64 21 380 7162</li>
          <li><span class="contact__key">M</span>+64 9 615 4308</li>
          <li><span class="contact__key">E</span>martin@k7group.co.nz</li>
        </ul>
      </div>

      <p class="web">www.<strong>k7group</strong>.co.nz</p>

      <div class="accent-band">
        <span class="accent-band__dark"></span>
        <span class="accent-band__red"></span>
      </div>
    </section>
  </main>
</body>
</html>
```